Business Profile Landing Page for search engine Start UP " Ember Gate"

Hi there
Ember Gate is an search engine for the Ember Gate - business.

What i´m looking for is a stunning singel Profile Landing Page for the Companys presentation.

Following Details should be included.

1st section
Comapanys name
Adress
info row ( opening time or what ever)
Profile Picture Big ( Could be the logo)
+3 smaller Pictures ( Maybe the store, main product ...)

2nd Section
navigation Icons for:
Call, Mail , Web, Route, Data

3er Section
About us.

Text lines.....
+Pictures slider

4th Section
1 row : Products ( Titel , Picture, Price)
2nd row :Service ( same as Products + text lines )

5th section
Blog Posts row

.....................................................
Well thats all, Colors used from the logo, u can also use the favicon somewhere (the crown magnifying glass)

Target Market(s)

All Comapnys, it should be an " used for all" design

Number of Pages Required

1 page

Requirements
Must have
• The first sighting is the important part, so the " first section should be impressively and makes the customers curious about more informations (very important for mobile version)
Nice to have
• If you can insert our favicon somewhere would be cool, but its not nessesery
Should not have
• you dont need to make a header or footer, that part is already done. i just need the main section design

```html
<!DOCTYPE html>
<html lang="en">
<head>
<meta charset="utf-8">
<title>Ember Gate – Business Profile</title>
<link href="https://fonts.googleapis.com/css2?family=Nunito:wght@600;700;800&family=Mulish:wght@400;600;700&display=swap" rel="stylesheet">
<style>
:root{
  --gold:#e19e00;
  --gold-deep:#c98a08;
  --band:#d4920b;
  --band-dark:#bf8208;
  --ink:#2a1512;
  --night:#1b1210;
  --text:#444;
  --muted:#666;
  --paper:#fff;
  --mist:#f2f2f2;
}
*{box-sizing:border-box;margin:0;padding:0}
html,body{width:1200px;height:3910px;overflow:hidden}
body{font-family:"Mulish",sans-serif;color:var(--text);background:var(--paper);position:relative}
h1,h2,h3,.brand{font-family:"Nunito",sans-serif}
.abs{position:absolute}

/* header */
.site-header{position:absolute;left:0;top:0;width:1200px;height:97px;background:#fff}
.brand{position:absolute;left:95px;top:18px}
.brand-name{font-size:30px;font-weight:800;color:var(--gold);line-height:1}
.brand-sub{font-family:"Mulish",sans-serif;font-size:18px;color:#222;margin-top:4px}
.main-nav{position:absolute;right:105px;top:42px;display:flex;gap:50px;font-size:13px;color:#222;text-transform:uppercase}

/* hero */
.hero{position:absolute;left:0;top:97px;width:1200px;height:634px;background:#000;overflow:hidden}
.hero-photo{position:absolute;left:0;top:0;width:1200px;height:634px;
  background:linear-gradient(90deg,#8a6b52 0%,#a7876b 25%,#6d5443 45%,#2b211b 60%,#000 72%)}
.hero-arrow{position:absolute;top:245px}
.hero-info{position:absolute;left:693px;top:90px;width:380px;color:#fff}
.hero-title{font-size:66px;font-weight:800;color:var(--gold);line-height:1;padding-bottom:10px;border-bottom:2px solid var(--gold)}
.hero-tag{font-family:"Nunito",sans-serif;font-size:31px;font-weight:600;margin-top:10px}
.hero-text{font-size:16px;line-height:23px;margin-top:18px;color:#eee}
.hero-row{display:flex;align-items:flex-start;gap:14px;margin-top:26px;font-size:19px;line-height:28px}
.hero-row.small{font-size:17px;margin-top:30px}

/* store cards */
.store-cards{position:absolute;left:121px;top:645px;width:964px;height:264px;display:flex}
.store-card{flex:1;display:flex;flex-direction:column}
.store-photo{flex:1}
.store-bar{height:55px;display:flex;align-items:center;justify-content:space-between;padding:0 14px 0 38px;color:#fff;font-weight:700;font-size:18px;text-transform:uppercase}
.store-bar.dark{background:var(--ink)}
.store-bar.gold{background:var(--gold)}
.chev{width:26px;height:26px;border-radius:50%;background:#fff;display:flex;align-items:center;justify-content:center}

/* quick actions */
.quick-actions{position:absolute;left:0;top:1000px;width:1200px;height:240px}
.action{position:absolute;top:60px;width:158px;height:158px;border-radius:50%;background:#fff;box-shadow:0 3px 10px rgba(0,0,0,.12);display:flex;align-items:center;justify-content:center}
.action::before{content:"";position:absolute;left:10px;top:-14px;width:138px;height:70px;border-radius:70px 70px 0 0;background:var(--gold);z-index:0}
.action-core{position:relative;z-index:1;width:136px;height:136px;border-radius:50%;background:var(--ink);border:5px solid #fff;display:flex;flex-direction:column;align-items:center;justify-content:center;color:#fff;font-size:17px;gap:10px}

/* about */
.about{position:absolute;left:0;top:1300px;width:1200px;height:492px;background:linear-gradient(#fff 0%,var(--mist) 55%,var(--mist) 100%);text-align:center}
.section-title{font-size:43px;font-weight:700;color:#111}
.section-title span{color:var(--gold-deep)}
.about .section-title{margin-top:55px}
.about p{width:880px;margin:0 auto;font-size:16px;line-height:28px;color:var(--text)}
.about p.first{margin-top:24px}
.about p+p{margin-top:32px}
.btn{display:inline-block;border-radius:30px;font-size:15px;font-weight:600;color:#fff;text-transform:uppercase}
.about .btn{margin-top:56px;background:var(--gold-deep);width:184px;height:50px;line-height:50px}

/* gallery */
.gallery{position:absolute;left:0;top:1792px;width:1200px;height:267px;display:flex;gap:4px}
.gallery-item{flex:1}
.gal-arrow{position:absolute;top:118px}

/* products */
.products{position:absolute;left:0;top:2059px;width:1200px;height:517px}
.products .section-title{position:absolute;top:70px;width:1200px;text-align:center;font-size:34px}
.product{position:absolute;top:147px;width:240px;height:299px;border:1px solid var(--gold);background:#fff;padding:9px}
.product-inner{height:100%;box-shadow:0 0 8px rgba(0,0,0,.12);display:flex;flex-direction:column;align-items:center}
.product-photo{width:170px;height:150px;margin-top:32px;border-radius:8px}
.product-name{margin-top:36px;font-size:16px;font-weight:700;color:#222}
.product-price{margin-top:8px;font-size:20px;font-weight:600;color:var(--gold-deep)}

/* services */
.services{position:absolute;left:0;top:2576px;width:1200px;height:522px;background:linear-gradient(var(--band),var(--band-dark))}
.services .section-title{position:absolute;top:82px;width:1200px;text-align:center;color:#fff;font-size:34px}
.service{position:absolute;top:147px;width:223px;height:284px;background:#b87c06;text-align:center;color:#fff}
.service-photo{height:167px}
.service h3{font-size:17px;font-weight:700;margin-top:16px}
.service p{font-size:11.5px;line-height:18px;margin:8px auto 0;width:190px;color:#f6e6c4}
.service .chev{margin:12px auto 0;width:30px;height:30px}

/* blog */
.blog{position:absolute;left:0;top:3098px;width:1200px;height:617px}
.blog .section-title{position:absolute;left:115px;top:58px;font-size:34px}
.post{position:absolute;top:129px;width:304px;height:405px;background:#fff;box-shadow:0 2px 10px rgba(0,0,0,.15);text-align:center}
.post-photo{height:185px}
.post-date{font-size:14px;margin-top:28px;color:#222}
.post h3{font-size:18px;font-weight:700;color:#111;margin-top:8px}
.post p{font-size:11.5px;line-height:20px;width:270px;margin:10px auto 0;color:var(--muted)}
.post .btn{margin-top:18px;width:128px;height:34px;line-height:34px;font-size:12px;background:var(--gold-deep)}
.post.featured{background:var(--gold-deep);color:#fff}
.post.featured .post-date,.post.featured h3{color:#fff}
.post.featured p{color:#f3e0b8}
.post.featured .btn{background:#111}

/* footer */
.site-footer{position:absolute;left:0;top:3715px;width:1200px;height:195px;background:var(--night);text-align:center;color:#bbb}
.copyright{font-size:14px;margin-top:52px}
.social{display:flex;justify-content:center;gap:10px;margin-top:26px}
.social span{width:35px;height:35px;border-radius:50%;background:#fff}
</style>
</head>
<body>

<header class="site-header">
  <div class="brand">
    <div class="brand-name">Ember Gate</div>
    <div class="brand-sub">Floristen &amp; Gärtner</div>
  </div>
  <nav class="main-nav">
    <span style="color:var(--gold-deep)">Home</span><span>About us</span><span>Products</span><span>Our services</span><span>Blogs</span><span>Contact</span>
  </nav>
</header>

<section class="hero">
  <div class="hero-photo" role="img" aria-label="Couple smiling while working on a laptop at a table"></div>
  <svg class="hero-arrow" style="left:48px" width="30" height="56" viewBox="0 0 30 56"><path d="M28 2 2 28l26 26" fill="none" stroke="#fff" stroke-width="2"/></svg>
  <svg class="hero-arrow" style="left:1130px" width="30" height="56" viewBox="0 0 30 56"><path d="M2 2l26 26L2 54" fill="none" stroke="#fff" stroke-width="2"/></svg>
  <div class="hero-info">
    <h1 class="hero-title">Ember Gate</h1>
    <div class="hero-tag">Floristen &amp; Gartner</div>
    <p class="hero-text">Sed ut perspiciatis unde omnis iste natus error sit oluptatem accusantium doloremque</p>
    <div class="hero-row">
      <svg width="22" height="28" viewBox="0 0 22 28"><path d="M11 1C5.5 1 1 5.3 1 10.8 1 18 11 27 11 27s10-9 10-16.2C21 5.3 16.5 1 11 1z" fill="#fff"/><circle cx="11" cy="10.5" r="4" fill="#000"/></svg>
      <span>123 Avenue name, City name<br>25252, United States</span>
    </div>
    <div class="hero-row small">
      <svg width="24" height="24" viewBox="0 0 24 24"><circle cx="12" cy="12" r="10.5" fill="none" stroke="#fff" stroke-width="2"/><path d="M12 6v6h5" fill="none" stroke="#fff" stroke-width="2"/></svg>
      <span>Opening Time: 8 am to 7 pm</span>
    </div>
  </div>
</section>

<div class="store-cards">
  <div class="store-card">
    <div class="store-photo" role="img" aria-label="Grey armchair beside a wooden sideboard" style="background:linear-gradient(#e9eaeb,#b9b6b1)"></div>
    <div class="store-bar dark">Store product<span class="chev"><svg width="12" height="12" viewBox="0 0 12 12"><path d="M2 2l4 4-4 4M6 2l4 4-4 4" fill="none" stroke="var(--gold)" stroke-width="1.6"/></svg></span></div>
  </div>
  <div class="store-card">
    <div class="store-photo" role="img" aria-label="Wristwatch resting on a notebook" style="background:linear-gradient(135deg,#f2f3f4,#8c9298 60%,#2d3136)"></div>
    <div class="store-bar gold">Store product<span class="chev"><svg width="12" height="12" viewBox="0 0 12 12"><path d="M2 2l4 4-4 4M6 2l4 4-4 4" fill="none" stroke="var(--gold)" stroke-width="1.6"/></svg></span></div>
  </div>
  <div class="store-card">
    <div class="store-photo" role="img" aria-label="Desktop computer on a desk with a small plant" style="background:linear-gradient(#f4f4f5,#dcdcdc 70%,#cdb89a)"></div>
    <div class="store-bar gold">Store product<span class="chev"><svg width="12" height="12" viewBox="0 0 12 12"><path d="M2 2l4 4-4 4M6 2l4 4-4 4" fill="none" stroke="var(--gold)" stroke-width="1.6"/></svg></span></div>
  </div>
</div>

<section class="quick-actions">
  <div class="action" style="left:133px"><div class="action-core">
    <svg width="34" height="34" viewBox="0 0 24 24" fill="none" stroke="#fff" stroke-width="1.8"><path d="M5 3h4l2 5-2.5 1.5a11 11 0 0 0 6 6L16 13l5 2v4a2 2 0 0 1-2 2A17 17 0 0 1 3 5a2 2 0 0 1 2-2z"/><path d="M14 3a7 7 0 0 1 7 7M14 7a3 3 0 0 1 3 3"/></svg>CALL</div></div>
  <div class="action" style="left:334px"><div class="action-core">
    <svg width="40" height="30" viewBox="0 0 40 30" fill="none" stroke="#fff" stroke-width="2"><rect x="2" y="2" width="36" height="26" rx="2"/><path d="M2 4l18 13L38 4"/></svg>MAIL</div></div>
  <div class="action" style="left:532px"><div class="action-core">
    <svg width="40" height="32" viewBox="0 0 40 32" fill="none" stroke="#fff" stroke-width="2"><rect x="2" y="2" width="36" height="28" rx="2"/><path d="M2 9h36M7 15h26M7 20h12M7 25h12M23 20h10v5H23z"/></svg>WEB</div></div>
  <div class="action" style="left:730px"><div class="action-core">
    <svg width="40" height="34" viewBox="0 0 40 34" fill="none" stroke="#fff" stroke-width="2"><circle cx="6" cy="6" r="4"/><circle cx="34" cy="28" r="4"/><path d="M10 6h18a6 6 0 0 1 0 12H12a5 5 0 0 0 0 10h18"/></svg>ROUTE</div></div>
  <div class="action" style="left:925px"><div class="action-core">
    <svg width="34" height="38" viewBox="0 0 34 38" fill="none" stroke="#fff" stroke-width="2"><ellipse cx="17" cy="6" rx="15" ry="4.5"/><path d="M2 6v26c0 2.5 6.7 4.5 15 4.5S32 34.5 32 32V6M2 15c0 2.5 6.7 4.5 15 4.5S32 17.5 32 15M2 24c0 2.5 6.7 4.5 15 4.5S32 26.5 32 24"/></svg>DATA</div></div>
</section>

<section class="about">
  <h2 class="section-title">About <span>Ember Gate</span></h2>
  <p class="first">Sed ut perspiciatis unde omnis iste natus error sit voluptatem accusantium doloremque laudantium, totam rem aperiam, eaque ipsa quae ab illo inventore veritatis et quasi architecto beatae vitae dicta sunt explicabo.</p>
  <p>Nemo enim ipsam voluptatem quia Voluptas sit aspernatur aut odit aut fugit, sed quia consequuntur magni dolores eos qui ratione voluptatem sequi nesciunt. Neque porro quisquam est, qui dolorem ipsum quia dolor sit amet, consectetur, adipisci velit, sed quia non numquam eius modi</p>
  <span class="btn">Learn more</span>
</section>

<section class="gallery">
  <div class="gallery-item" role="img" aria-label="Hands typing on a laptop" style="background:linear-gradient(135deg,#3b3f44,#9ea3a8 60%,#d8d8d6)"></div>
  <div class="gallery-item" role="img" aria-label="Bouquet of autumn flowers" style="background:radial-gradient(circle at 50% 45%,#c9663e,#a34a2c 40%,#3d4a36 80%)"></div>
  <div class="gallery-item" role="img" aria-label="Notebook sketch about search optimisation on a wooden desk" style="background:radial-gradient(circle,#efece4 40%,#b98a52 90%)"></div>
  <div class="gallery-item" role="img" aria-label="Two people looking at a laptop together" style="background:linear-gradient(135deg,#dfe3e6,#7f8a96 55%,#c9b7a8)"></div>
  <svg class="gal-arrow" style="left:22px" width="24" height="42" viewBox="0 0 24 42"><path d="M22 2 3 21l19 19" fill="none" stroke="#fff" stroke-width="3"/></svg>
  <svg class="gal-arrow" style="left:1146px" width="24" height="42" viewBox="0 0 24 42"><path d="M2 2l19 19L2 40" fill="none" stroke="#fff" stroke-width="3"/></svg>
</section>

<section class="products">
  <h2 class="section-title">Our Products</h2>
  <div class="product" style="left:91px"><div class="product-inner">
    <div class="product-photo" role="img" aria-label="Pink flowers in a wooden planter" style="background:radial-gradient(circle,#e06a9a,#5f8a3a 60%,#fff 72%)"></div>
    <div class="product-name">PRODUCT NAME</div><div class="product-price">$30.00</div></div></div>
  <div class="product" style="left:349px"><div class="product-inner">
    <div class="product-photo" role="img" aria-label="Kitchen blender" style="background:radial-gradient(ellipse 30% 50%,#9aa0a6,#dfe2e5 70%,#fff 100%)"></div>
    <div class="product-name">PRODUCT NAME</div><div class="product-price">$30.00</div></div></div>
  <div class="product" style="left:607px"><div class="product-inner">
    <div class="product-photo" role="img" aria-label="Black smartwatch" style="background:radial-gradient(circle,#2c2c2e,#5a5a5c 45%,#fff 70%)"></div>
    <div class="product-name">PRODUCT NAME</div><div class="product-price">$30.00</div></div></div>
  <div class="product" style="left:866px"><div class="product-inner">
    <div class="product-photo" role="img" aria-label="Purple flowers in a yellow pot" style="background:radial-gradient(circle,#7a6fd0,#4b7a34 50%,#e6d84a 62%,#fff 75%)"></div>
    <div class="product-name">PRODUCT NAME</div><div class="product-price">$30.00</div></div></div>
</section>

<section class="services">
  <h2 class="section-title">Our Services</h2>
  <div class="service" style="left:96px">
    <div class="service-photo" role="img" aria-label="Laptop showing a search optimisation graphic" style="background:linear-gradient(135deg,#d8a07a,#4a8fa0 50%,#d9d2c4)"></div>
    <h3>Aultricies orci</h3><p>elerisque mi tortor at ipsum Proin orci odio commodo ac</p>
    <div class="chev"><svg width="14" height="14" viewBox="0 0 12 12"><path d="M2 2l4 4 4-4M2 6l4 4 4-4" fill="none" stroke="var(--gold)" stroke-width="1.6"/></svg></div></div>
  <div class="service" style="left:350px">
    <div class="service-photo" role="img" aria-label="Hand on a keyboard with digital icons" style="background:linear-gradient(135deg,#4a4a48,#8b8b86 50%,#2e2e2c)"></div>
    <h3>Tristique hendrerit</h3><p>elerisque mi tortor at ipsum Proin orci odio commodo ac</p>
    <div class="chev"><svg width="14" height="14" viewBox="0 0 12 12"><path d="M2 2l4 4 4-4M2 6l4 4 4-4" fill="none" stroke="var(--gold)" stroke-width="1.6"/></svg></div></div>
  <div class="service" style="left:604px">
    <div class="service-photo" role="img" aria-label="Phone held in hand with network icons" style="background:linear-gradient(135deg,#c9c7c2,#6a6f74 50%,#3a3d40)"></div>
    <h3>Felis vitae urna</h3><p>elerisque mi tortor at ipsum Proin orci odio commodo ac</p>
    <div class="chev"><svg width="14" height="14" viewBox="0 0 12 12"><path d="M2 2l4 4 4-4M2 6l4 4 4-4" fill="none" stroke="var(--gold)" stroke-width="1.6"/></svg></div></div>
  <div class="service" style="left:858px">
    <div class="service-photo" role="img" aria-label="Person working with a calculator and documents" style="background:linear-gradient(135deg,#6d7782,#b9c2c8 50%,#4b5a50)"></div>
    <h3>Aultricies orci</h3><p>elerisque mi tortor at ipsum Proin orci odio commodo ac</p>
    <div class="chev"><svg width="14" height="14" viewBox="0 0 12 12"><path d="M2 2l4 4 4-4M2 6l4 4 4-4" fill="none" stroke="var(--gold)" stroke-width="1.6"/></svg></div></div>
</section>

<section class="blog">
  <h2 class="section-title">Recent <span style="color:var(--gold-deep)">Blog Posts</span></h2>
  <article class="post" style="left:112px">
    <div class="post-photo" role="img" aria-label="Laptop with charts on a desk" style="background:linear-gradient(135deg,#3d3a36,#a9a6a0 55%,#e7e5e1)"></div>
    <div class="post-date">📅 25 Aug 2020</div><h3>Lorem ipsum blog heading</h3>
    <p>Fusce ultricies orci ac feugiat suscipit leo massa sodales velit et scelerisque mi tortor at ipsum Proin orci odio commodo ac gravida</p>
    <span class="btn">Learn more</span></article>
  <article class="post featured" style="left:431px">
    <div class="post-photo" role="img" aria-label="Hands holding a smartphone in warm light" style="background:linear-gradient(135deg,#f0c77a,#c98a58 50%,#6b4a32)"></div>
    <div class="post-date">📅 10 Aug 2020</div><h3>Lorem ipsum blog heading</h3>
    <p>Fusce ultricies orci ac feugiat suscipit leo massa sodales velit et scelerisque mi tortor at ipsum Proin orci odio commodo ac</p>
    <span class="btn">Learn more</span></article>
  <article class="post" style="left:751px">
    <div class="post-photo" role="img" aria-label="Notes about search optimisation beside glasses and a cup" style="background:linear-gradient(135deg,#8a7050,#e9e4d8 50%,#5c7a3c)"></div>
    <div class="post-date">📅 05 Aug 2020</div><h3>Lorem ipsum blog heading</h3>
    <p>Fusce ultricies orci ac feugiat suscipit leo massa sodales velit et scelerisque mi tortor at ipsum Proin orci odio commodo ac</p>
    <span class="btn">Learn more</span></article>
</section>

<footer class="site-footer">
  <div class="copyright">© Copyright 2020 . Ember Gate All Right Reserved</div>
  <div class="social" aria-label="Social links"><span></span><span></span><span></span><span></span></div>
</footer>

</body>
</html>
```